Modern card design needed for building development company

We are looking for a sharp modern new look for our business cards.
We are a New Zealand based company called TKR Ventures NZ LTD that specialises in subdividing large sections, housing and commercial buildings.
We have attached a photo of the current logo and would like to see it improved somehow as it looks a bit dated.
We are open to any colours.

Target Market(s)

Investors, Property buyers

Industry/Entity Type

Investment

Contact Information for Business Card

TKR VENTURES NZ LTD
www.tkrventuresnz.example.nz

Dorian Fletcher
Phone +64 21 843 209
Email dpfletcher@mailvane.example.nz

Font styles to use
Serif
Sans Serif

Colors
0792cd
33a6d7
85cae6
6b449b
886aae
f04a50
ec1f27
f37122
f68d4d

Requirements
Must have
• Please try and make the logo more modern or if you have a similar one we would like to see it.

```html
<!DOCTYPE html>
<html lang="en">
<head>
<meta charset="utf-8">
<title>TKR Ventures NZ LTD – Business Card</title>
<link rel="stylesheet" href="https://fonts.googleapis.com/css2?family=Oswald:wght@600&family=Open+Sans:wght@400&display=swap">
<style>
  :root {
    --backdrop: #2b2b2d;
    --card-white: #ffffff;
    --frame-purple: #6b449b;
    --accent-blue: #33a6d7;
    --ink-dark: #2a2a2a;
    --ink-body: #333333;
    --panel-light: #f4f4f4;
    --panel-shade: #d9d9d9;
    --divider: #b5b5b5;
  }
  * { box-sizing: border-box; margin: 0; padding: 0; }
  html, body { width: 1200px; height: 900px; overflow: hidden; }
  body {
    background: var(--backdrop);
    display: flex;
    flex-direction: column;
    align-items: center;
    justify-content: center;
    gap: 40px;
    font-family: "Open Sans", Arial, sans-serif;
  }
  .card {
    width: 700px;
    height: 400px;
    position: relative;
    box-shadow: 0 12px 30px rgba(0,0,0,0.45);
  }

  /* Front */
  .card-front {
    background: var(--card-white);
    display: flex;
    flex-direction: column;
    align-items: center;
    justify-content: center;
    gap: 10px;
  }
  .brand {
    display: flex;
    align-items: center;
    gap: 14px;
  }
  .brand-mark {
    width: 34px;
    height: 34px;
    background: var(--accent-blue);
  }
  .brand-name {
    font-family: "Oswald", "Arial Narrow", sans-serif;
    font-weight: 600;
    font-size: 36px;
    letter-spacing: 0.5px;
    color: var(--ink-dark);
  }
  .front-url {
    font-size: 21px;
    letter-spacing: 1px;
    color: var(--ink-body);
  }

  /* Back */
  .card-back {
    background: var(--frame-purple);
    padding: 26px;
  }
  .back-panel {
    width: 100%;
    height: 100%;
    background: radial-gradient(ellipse at 50% 40%, var(--panel-light) 0%, #e8e8e8 55%, var(--panel-shade) 100%);
    display: flex;
    align-items: center;
    position: relative;
  }
  .back-brand {
    width: 57%;
    display: flex;
    justify-content: center;
  }
  .back-brand .brand-name { font-size: 30px; }
  .back-brand .brand-mark { width: 28px; height: 28px; }
  .divider {
    position: absolute;
    left: 57%;
    top: 60px;
    bottom: 60px;
    width: 1px;
    background: var(--divider);
  }
  .contact-list {
    list-style: none;
    padding-left: 18px;
    display: flex;
    flex-direction: column;
    gap: 8px;
  }
  .contact-item {
    display: flex;
    align-items: flex-start;
    gap: 8px;
    font-size: 12.5px;
    line-height: 1.35;
    color: var(--ink-body);
  }
  .contact-icon {
    width: 14px;
    height: 14px;
    flex: none;
    margin-top: 2px;
    fill: var(--frame-purple);
  }
</style>
</head>
<body>

  <section class="card card-front" aria-label="Card front">
    <div class="brand">
      <span class="brand-mark"></span>
      <span class="brand-name">TKR VENTURES NZ LTD</span>
    </div>
    <p class="front-url">www.tkrventuresnz.example.nz</p>
  </section>

  <section class="card card-back" aria-label="Card back">
    <div class="back-panel">
      <div class="back-brand">
        <div class="brand">
          <span class="brand-mark"></span>
          <span class="brand-name">TKR VENTURES NZ LTD</span>
        </div>
      </div>
      <span class="divider"></span>
      <ul class="contact-list">
        <li class="contact-item">
          <svg class="contact-icon" viewBox="0 0 24 24" aria-hidden="true"><path d="M6.6 10.8a15.1 15.1 0 0 0 6.6 6.6l2.2-2.2c.3-.3.7-.4 1-.2 1.1.4 2.3.6 3.6.6.6 0 1 .4 1 1V20c0 .6-.4 1-1 1A17 17 0 0 1 3 4c0-.6.4-1 1-1h3.5c.6 0 1 .4 1 1 0 1.3.2 2.5.6 3.6.1.3 0 .7-.2 1z"/></svg>
          <span>+64 21 843 209</span>
        </li>
        <li class="contact-item">
          <svg class="contact-icon" viewBox="0 0 24 24" aria-hidden="true"><path d="M3 5h18v14H3z M4.5 6.5 12 12l7.5-5.5" fill="none" stroke="#6b449b" stroke-width="2"/></svg>
          <span>dpfletcher@mailvane.example.nz</span>
        </li>
        <li class="contact-item">
          <svg class="contact-icon" viewBox="0 0 24 24" aria-hidden="true"><g fill="none" stroke="#6b449b" stroke-width="2"><circle cx="12" cy="12" r="9"/><path d="M3 12h18M12 3c3 3 3 15 0 18M12 3c-3 3-3 15 0 18"/></g></svg>
          <span>www.tkrventuresnz.example.nz</span>
        </li>
        <li class="contact-item">
          <svg class="contact-icon" viewBox="0 0 24 24" aria-hidden="true"><path d="M12 2a7 7 0 0 0-7 7c0 5.2 7 13 7 13s7-7.8 7-13a7 7 0 0 0-7-7zm0 9.5A2.5 2.5 0 1 1 12 6.5a2.5 2.5 0 0 1 0 5z"/></svg>
          <span>PO BOX 48215, Northcote<br>Auckland, New Zealand</span>
        </li>
      </ul>
    </div>
  </section>

</body>
</html>
```